I am looking for label for our Candle Company

We need a label design for our new Candle Company based in Kansas City called Brisa Lumel Candle Company. (Pronounced "Fla-May"). We want to make sure we get the tick above the "e" in Brisa as Brisa is french for flame. We need a logo that we can use on the candles. We need it to include our name but we need to be able to edit the individual candle scent.

We are looking for a very elegant and vintage/old french look. We do not really want a lot (if any) bright color to the logo/design. I have enclosed our current log (of which we don't really like but are temporarily using) and a design that we love and would like to incorporate. You can see on our current label how we have to be able to include the individual candle scent name. I need to be able to edit this name.
Updates

Ilse, We have a couple of different label applications that we need to use the design on. We have a small label, a large label and a round label. I will work on getting you the dimensions tomorrow. Do you think there is any way to make a logo out of the middle part of this label? Doug

Target Market(s)

Anyone who loves candles.

Industry/Entity Type

It Company

Logo Text

Brisa Lumel Candle Company

Font styles to use
Decorative
Script

Requirements
Must have
• The ability to edit the candle scent name so that we can use it on every different candle that we make.
Should not have
• Too many vibrant colors.

```html
<!DOCTYPE html>
<html lang="en">
<head>
<meta charset="utf-8">
<title>Brisa Lumel Candle Company – Label</title>
<link rel="stylesheet" href="https://fonts.googleapis.com/css2?family=Pinyon+Script&family=EB+Garamond&display=swap">
<style>
  :root {
    --paper: #ffffff;
    --peach: #e8c3a6;
    --dusk: #a7939f;
    --plum: #785773;
    --cartouche: #e6bea2;
    --ink: #2a1f22;
    --cream: #fbf3ec;
  }
  html, body {
    margin: 0;
    padding: 0;
    overflow: hidden;
    background: var(--paper);
  }
  .label {
    position: relative;
    width: 1200px;
    height: 378px;
    overflow: hidden;
    background: var(--paper);
  }
  .label__band {
    position: absolute;
    left: 0;
    top: 16px;
    width: 1200px;
    height: 346px;
    background: linear-gradient(to bottom, var(--peach) 0%, var(--dusk) 55%, var(--plum) 100%);
  }
  .label__frame {
    position: absolute;
    left: 426px;
    top: 26px;
    width: 348px;
    height: 296px;
  }
  .label__name {
    position: absolute;
    left: 0;
    width: 1200px;
    text-align: center;
    font-family: "Pinyon Script", cursive;
    font-size: 42px;
    line-height: 1;
    color: var(--ink);
    margin: 0;
  }
  .label__name--first { top: 126px; }
  .label__name--second { top: 180px; }
  .label__scent {
    position: absolute;
    left: 0;
    top: 244px;
    width: 1200px;
    text-align: center;
    font-family: "EB Garamond", serif;
    font-size: 29px;
    line-height: 1;
    color: var(--cream);
    margin: 0;
  }
  .label__mark {
    position: absolute;
    left: 0;
    top: 328px;
    width: 1200px;
    text-align: center;
    font-family: "Pinyon Script", cursive;
    font-size: 20px;
    line-height: 1;
    color: var(--ink);
    margin: 0;
  }
</style>
</head>
<body>
  <main class="label">
    <div class="label__band" role="img" aria-label="Fine diamond lattice pattern over a peach to plum gradient"></div>

    <svg class="label__frame" viewBox="0 0 348 296" role="img" aria-label="Baroque scroll cartouche framing the company name">
      <path d="M40 40 Q174 -10 308 40 Q348 148 308 256 Q174 306 40 256 Q0 148 40 40 Z"
            fill="var(--cartouche)" stroke="var(--ink)" stroke-width="1.5"/>
    </svg>

    <h1 class="label__name label__name--first">Brisa Lumel</h1>
    <p class="label__name label__name--second">Candle Company</p>
    <p class="label__scent">Girls night out</p>
    <p class="label__mark">Brisa Lumel</p>
  </main>
</body>
</html>
```